Love pets? Create a veterinary business card that aligns with our new revamped website.

Greetings! We are a five-doctor veterinary hospital that seeks your expertise in designing a new business card that harmonizes with our recently revitalized website: www.tqrn.net. The card should feature our logo, the five doctors, operating hours, contact information, and communicate our purpose and personality.

Contact Information for Business Card

TBA

```html
<!DOCTYPE html>
<html lang="en">
<head>
<meta charset="utf-8">
<title>Maple Hollow Veterinary Hospital – Business Card</title>
<link rel="stylesheet" href="https://fonts.googleapis.com/css2?family=Dancing+Script:wght@600&family=Roboto:wght@400;500&display=swap">
<style>
  :root {
    --stage: #474747;
    --card-white: #ffffff;
    --card-black: #171717;
    --brand-green: #3f8a32;
    --brand-gold: #9a6a1f;
    --ink: #1f1f1f;
  }
  * { box-sizing: border-box; margin: 0; padding: 0; }
  html, body {
    width: 1200px; height: 801px; overflow: hidden;
    background: var(--stage);
    font-family: "Roboto", Arial, sans-serif;
  }
  .stage {
    width: 1200px; height: 801px;
    display: flex; align-items: center; justify-content: center; gap: 48px;
  }
  .card {
    width: 530px; height: 303px; position: relative;
    box-shadow: 0 14px 30px rgba(0,0,0,.35);
  }
  .card--front {
    background: var(--card-white);
    border-bottom: 3px solid var(--brand-green);
    border-left: 3px solid var(--brand-green);
    display: flex; align-items: center;
  }
  .card--back {
    background: var(--card-black);
    border-bottom: 3px solid var(--brand-green);
    border-left: 3px solid var(--brand-green);
    display: flex; align-items: center; justify-content: center;
  }
  .brand {
    display: flex; align-items: center; gap: 10px;
    color: var(--brand-green); font-weight: 500;
  }
  .brand__dot {
    border-radius: 50%; background: var(--brand-green); flex: none;
  }
  .brand__name { line-height: 1.15; }
  .card--front .brand { width: 265px; padding-left: 40px; }
  .card--front .brand__dot { width: 26px; height: 26px; }
  .card--front .brand__name { font-size: 17px; }
  .card--back .brand { gap: 18px; }
  .card--back .brand__dot { width: 60px; height: 60px; }
  .card--back .brand__name { font-size: 32px; }
  .divider {
    width: 1.5px; height: 190px; background: var(--brand-green); flex: none;
  }
  .contact { padding-left: 26px; color: var(--ink); }
  .contact__name {
    font-family: "Dancing Script", cursive; font-weight: 600;
    color: var(--brand-green); font-size: 24px; letter-spacing: .5px;
  }
  .contact__role { font-size: 14px; margin-bottom: 10px; }
  .contact__list { list-style: none; font-size: 14px; line-height: 1.45; }
  .contact__list li { display: flex; align-items: center; gap: 7px; }
  .contact__list svg { width: 12px; height: 12px; fill: var(--brand-green); flex: none; }
  .contact__address { font-size: 14px; line-height: 1.4; margin-top: 14px; }
</style>
</head>
<body>
<main class="stage">
  <section class="card card--front" aria-label="Business card front">
    <div class="brand">
      <span class="brand__dot"></span>
      <span class="brand__name">Maple Hollow<br>Veterinary Hospital</span>
    </div>
    <span class="divider"></span>
    <div class="contact">
      <p class="contact__name">DAN PORTER</p>
      <p class="contact__role">Managing Director</p>
      <ul class="contact__list">
        <li><svg viewBox="0 0 24 24"><path d="M6.6 10.8a15.1 15.1 0 0 0 6.6 6.6l2.2-2.2c.3-.3.7-.4 1-.2 1.1.4 2.3.6 3.6.6.6 0 1 .4 1 1V20c0 .6-.4 1-1 1A17 17 0 0 1 3 4c0-.6.4-1 1-1h3.5c.6 0 1 .4 1 1 0 1.3.2 2.5.6 3.6.1.3 0 .7-.2 1z"/></svg>(555) 214-6082</li>
        <li><svg viewBox="0 0 24 24"><path d="M3 8h4v13H3zM9 3h8v5H9zM9 10h12v11H9zm3 2v2h2v-2zm4 0v2h2v-2zm-4 4v2h2v-2zm4 0v2h2v-2z"/></svg>(555) 306-7419</li>
        <li><svg viewBox="0 0 24 24"><path d="M2 5h20v14H2zm2 2v.5l8 5 8-5V7z"/></svg>info@tqrn.net</li>
        <li><svg viewBox="0 0 24 24"><path d="M12 2a10 10 0 1 0 0 20 10 10 0 0 0 0-20zm6.9 6h-3a15 15 0 0 0-1.3-3.9A8 8 0 0 1 18.9 8zM12 4c.8 1.2 1.5 2.5 1.9 4h-3.8c.4-1.5 1.1-2.8 1.9-4zM4.3 14a8 8 0 0 1 0-4h3.4a16 16 0 0 0 0 4zm.8 2h3a15 15 0 0 0 1.3 3.9A8 8 0 0 1 5.1 16zm3-8h-3a8 8 0 0 1 4.3-3.9C8.8 5.3 8.4 6.6 8.1 8zM12 20c-.8-1.2-1.5-2.5-1.9-4h3.8c-.4 1.5-1.1 2.8-1.9 4zm2.3-6H9.7a14 14 0 0 1 0-4h4.6a14 14 0 0 1 0 4zm.3 5.9c.6-1.2 1-2.5 1.3-3.9h3a8 8 0 0 1-4.3 3.9zm1.7-5.9a16 16 0 0 0 0-4h3.4a8 8 0 0 1 0 4z"/></svg>www.tqrn.net</li>
      </ul>
      <p class="contact__address">4820 Cedar Ridge Lane,<br>Brookfield, TX 75012</p>
    </div>
  </section>

  <section class="card card--back" aria-label="Business card back">
    <div class="brand">
      <span class="brand__dot"></span>
      <span class="brand__name">Maple Hollow<br>Veterinary Hospital</span>
    </div>
  </section>
</main>
</body>
</html>
```